Havenry - "Where Pest Control is Free for Life..." Please see pitch deck...

Project goal, that this is a reusable template, not a one-off card
Brand and design direction, follow the logo, use the brand palette (with a color swatch table), typography and layout guidance
The Mark Vale placeholder content as a clean field-by-field table (name, title, company, address, office, cell, fax, email, havenry.com)
Print specs, 3.5 × 2 in trim, 0.125 in bleed, 300 DPI, CMYK, crop marks
Deliverables, layered editable PSD (your primary ask) plus vector .AI/.EPS and a press-ready PDF/X-1a, with fonts packaged
What you'll provide (logo, colors, fonts)
Process and sign-off, concept first, then full file package on approval.
Populate every field with this Mark Vale placeholder data so we can see the layout fully built out. We will replace it per person.
Name Mark Vale
Title Title / Position
Company Havenry
Address 487 Orchard Lane, Suite 210, Tallahassee, FL 32308
Office (850) 555-0142
Cell (850) 555-0167
Fax (850) 555-0181
Email markvale@havenry.com
Website havenry.com

We need the working, editable source files so we can update them ourselves, plus a ready-to-print export:
1. Photoshop (.PSD) — fully layered and editable, with each contact field on its own labeled text layer. This is the primary requested format.
2. Vector source — the press-standard editable format, Adobe Illustrator (.AI) and/or .EPS, since vector is preferred for crisp text and logos at print.
3. Print-ready PDF — press-quality (PDF/X-1a), CMYK, with bleed and crop marks, both sides.
4. Packaged fonts and links — include or list all fonts used, and package any linked assets so the files open correctly on our end.

Why both PSD and vector
The PSD covers our request directly and is easy for us to edit. Vector (.AI/.EPS) is what most commercial printers actually prefer for type and logos because it stays razor-sharp at any size. Providing both keeps us flexible no matter which printer we use. Have fun and keep it modern and cool the designer of the logo did a great job, see what you can do.

```html
<!DOCTYPE html>
<html lang="en">
<head>
<meta charset="utf-8">
<title>Havenry Business Card</title>
<link href="https://fonts.googleapis.com/css2?family=Poppins:wght@400;500;700&display=swap" rel="stylesheet">
<style>
  :root {
    --backdrop: #a9a9a9;
    --navy: #0a1124;
    --teal: #00b2c6;
    --teal-soft: rgba(0, 178, 198, 0.28);
    --white: #ffffff;
    --ink: #2b2b2b;
  }
  * { margin: 0; padding: 0; box-sizing: border-box; }
  html, body {
    width: 935px; height: 1200px; overflow: hidden;
    background: var(--backdrop);
    font-family: "Poppins", sans-serif;
  }
  .canvas { position: relative; width: 935px; height: 1200px; }
  .card {
    position: absolute; left: 53px; width: 829px; height: 498px;
    overflow: hidden;
    box-shadow: 0 8px 22px rgba(0,0,0,.35);
  }
  .card--front { top: 73px; background: var(--navy); }
  .card--back { top: 624px; background: var(--white); }

  .graphic-area {
    position: absolute;
    background: linear-gradient(135deg, rgba(0,178,198,0) 0%, var(--teal-soft) 100%);
  }
  .card--front .graphic-area { left: 430px; top: 330px; width: 399px; height: 168px; }
  .back-band .graphic-area { left: 330px; top: 60px; width: 499px; height: 200px; }

  .front-brand {
    position: absolute; left: 160px; top: 170px; width: 500px;
    text-align: center;
  }
  .wordmark {
    font-weight: 700; color: var(--white); line-height: 1;
    letter-spacing: -1px;
  }
  .front-brand .wordmark { font-size: 84px; }
  .front-site {
    position: absolute; left: 160px; top: 358px; width: 500px;
    text-align: center; color: var(--white);
    font-size: 22px; letter-spacing: 3px; font-weight: 500;
  }
  .front-site strong { color: var(--teal); font-weight: 700; }

  .back-band {
    position: absolute; left: 0; top: 0; width: 829px; height: 260px;
    background: var(--navy); overflow: hidden;
  }
  .holder { position: absolute; left: 63px; top: 118px; }
  .holder-name {
    color: var(--teal); font-weight: 700; font-size: 53px;
    line-height: 1; letter-spacing: -0.5px;
  }
  .holder-title {
    color: var(--white); font-size: 26px; letter-spacing: 2px;
    margin-top: 4px; line-height: 1.1;
  }
  .back-brand { position: absolute; left: 552px; top: 172px; }
  .back-brand .wordmark { font-size: 50px; }

  .contact {
    position: absolute; display: flex; align-items: flex-start; gap: 9px;
    color: var(--ink); font-size: 17px; line-height: 23px;
  }
  .contact svg { width: 20px; height: 20px; flex: none; margin-top: 1px; fill: var(--teal); }
  .contact--office { left: 60px; top: 315px; }
  .contact--cell { left: 60px; top: 361px; }
  .contact--fax { left: 256px; top: 315px; }
  .contact--address { left: 256px; top: 361px; }
  .contact--email { left: 527px; top: 313px; }
  .contact--web { left: 527px; top: 359px; }
</style>
</head>
<body>
<div class="canvas">

  <section class="card card--front">
    <div class="graphic-area" role="img" aria-label="Decorative brand graphic in teal"></div>
    <div class="front-brand"><div class="wordmark">Havenry</div></div>
    <div class="front-site">www.<strong>havenry</strong>.com</div>
  </section>

  <section class="card card--back">
    <div class="back-band">
      <div class="graphic-area" role="img" aria-label="Decorative brand graphic in teal"></div>
      <div class="holder">
        <div class="holder-name">Mark Vale</div>
        <div class="holder-title">Title / Position</div>
      </div>
      <div class="back-brand"><div class="wordmark">Havenry</div></div>
    </div>

    <div class="contact contact--office">
      <svg viewBox="0 0 20 20" aria-hidden="true"><path d="M2 6c0-2 3-3 8-3s8 1 8 3v2h-4V6.5H6V8H2z"/><rect x="3" y="9" width="14" height="9" rx="2"/><circle cx="10" cy="13.5" r="2.6" fill="#fff"/></svg>
      <span>(850) 555-0142</span>
    </div>
    <div class="contact contact--cell">
      <svg viewBox="0 0 20 20" aria-hidden="true"><path d="M6 1h8a2 2 0 0 1 2 2v14a2 2 0 0 1-2 2H6a2 2 0 0 1-2-2V3a2 2 0 0 1 2-2zm0 2v13h8V3z"/><circle cx="10" cy="17.5" r=".9" fill="#fff"/></svg>
      <span>(850) 555-0167</span>
    </div>
    <div class="contact contact--fax">
      <svg viewBox="0 0 20 20" aria-hidden="true"><rect x="1" y="6" width="4" height="13" rx="1"/><path d="M6 7h13v12H6z"/><path d="M9 1h7v5H9z"/><g fill="#fff"><rect x="8" y="10" width="2" height="2"/><rect x="11" y="10" width="2" height="2"/><rect x="14" y="10" width="2" height="2"/><rect x="8" y="14" width="2" height="2"/><rect x="11" y="14" width="2" height="2"/><rect x="14" y="14" width="2" height="2"/></g></svg>
      <span>(850) 555-0181</span>
    </div>
    <div class="contact contact--address">
      <svg viewBox="0 0 20 20" aria-hidden="true"><path d="M10 1a6.5 6.5 0 0 1 6.5 6.5C16.5 12 10 19.5 10 19.5S3.5 12 3.5 7.5A6.5 6.5 0 0 1 10 1z"/><circle cx="10" cy="7.5" r="2.4" fill="#fff"/></svg>
      <span>487 Orchard Lane, Suite 210,<br>Tallahassee, FL 32308</span>
    </div>
    <div class="contact contact--email">
      <svg viewBox="0 0 20 20" aria-hidden="true"><path d="M1 4h18v13H1z"/><path d="M1.5 4.5 10 11l8.5-6.5M1.5 16.5 7.5 9.5M18.5 16.5l-6-7" stroke="#fff" stroke-width="1.3" fill="none"/></svg>
      <span>markvale@havenry.com</span>
    </div>
    <div class="contact contact--web">
      <svg viewBox="0 0 20 20" aria-hidden="true"><circle cx="10" cy="10" r="9"/><g stroke="#fff" stroke-width="1.1" fill="none"><ellipse cx="10" cy="10" rx="4" ry="9"/><path d="M1 10h18M2.5 5.5h15M2.5 14.5h15M10 1v18"/></g></svg>
      <span>www.havenry.com</span>
    </div>
  </section>

</div>
</body>
</html>
```